Toronto based company needs a logo and business card design

We are "Brellmont Restoration Corp.". A high rise building restoration company based in Toronto. We specialize in Building Envelope, Parking Garage and Waterproofing repairs. Would like to see designs which use the color Teal, Black and White or Red, Black and White. Prefer to have light color background for the front of the card and dark background for the reverse side. For logo design, we would prefer to see high rise building/s incorporated in it.

Industry/Entity Type

Construction

Logo Text

Brellmont

Font styles to use
Sans Serif

Colors
00a990
ffffff
ec1f27
85acd3
000000

```html
<!DOCTYPE html>
<html lang="en">
<head>
<meta charset="UTF-8">
<title>Brellmont Restoration Corp. – Business Card</title>
<link href="https://fonts.googleapis.com/css2?family=Lato:wght@400;700&display=swap" rel="stylesheet">
<style>
  :root {
    --backdrop: #262626;
    --card: #151515;
    --card-edge: #1d1d1d;
    --red: #ec1f27;
    --blue: #85acd3;
    --white: #ffffff;
    --silver: #8e8e8e;
  }
  * { margin: 0; padding: 0; box-sizing: border-box; }
  html, body { width: 1200px; height: 900px; overflow: hidden; }
  body {
    background: var(--backdrop);
    font-family: "Lato", Arial, sans-serif;
    position: relative;
  }
  .card {
    position: absolute;
    left: 280px;
    width: 640px;
    height: 366px;
    background: linear-gradient(135deg, var(--card) 0%, var(--card-edge) 70%, var(--card) 100%);
    box-shadow: 0 10px 30px rgba(0,0,0,0.5);
  }
  .card--back { top: 50px; }
  .card--front { top: 460px; }

  .wordmark {
    font-family: "Lato", Arial, sans-serif;
    font-weight: 700;
    text-transform: uppercase;
    line-height: 1.05;
  }
  .card--back .wordmark {
    position: absolute;
    left: 0; right: 0; top: 140px;
    text-align: center;
    color: var(--silver);
    font-size: 44px;
    letter-spacing: 3px;
  }
  .card--back .wordmark small {
    display: block;
    font-size: 22px;
    letter-spacing: 7px;
    margin-top: 4px;
  }

  .card--front .wordmark {
    position: absolute;
    left: 40px; top: 140px;
    width: 270px;
    color: var(--red);
    font-size: 40px;
    letter-spacing: 2px;
  }
  .card--front .wordmark small {
    display: block;
    font-size: 19px;
    letter-spacing: 4px;
    margin-top: 4px;
  }

  .divider {
    position: absolute;
    left: 330px; top: 100px;
    width: 2px; height: 165px;
    background: var(--white);
  }

  .contact {
    position: absolute;
    left: 356px; top: 100px;
    color: var(--white);
    font-size: 15px;
    line-height: 1.35;
  }
  .contact__name {
    color: var(--blue);
    font-size: 27px;
    text-transform: uppercase;
    letter-spacing: 1px;
    line-height: 1.1;
  }
  .contact__role { font-size: 15px; margin-bottom: 10px; }
  .contact__address { margin-bottom: 8px; }
  .contact__line {
    display: flex;
    align-items: center;
    gap: 9px;
    font-size: 15px;
  }
  .contact__line svg { width: 11px; height: 11px; flex: none; }
  .contact__web .domain { color: var(--blue); }
</style>
</head>
<body>

<section class="card card--back" aria-label="Card reverse">
  <div class="wordmark">Brellmont<small>Restoration Corp</small></div>
</section>

<section class="card card--front" aria-label="Card front">
  <div class="wordmark">Brellmont<small>Restoration Corp</small></div>
  <div class="divider"></div>
  <div class="contact">
    <div class="contact__name">Daniel Hartwell</div>
    <div class="contact__role">President</div>
    <div class="contact__address">418 Carrow Ave. suite 210,<br>Toronto, ON M4K 2B7</div>
    <div class="contact__line">
      <svg viewBox="0 0 12 12" aria-hidden="true"><path d="M2.5 1 L4.5 1 L5.2 3.5 L4 4.5 Q5 7 7.5 8 L8.5 6.8 L11 7.5 L11 9.5 Q10.5 11 9 11 Q1 10 1 2.5 Q1 1 2.5 1Z" fill="#85acd3"/></svg>
      <span>416-555-0148</span>
    </div>
    <div class="contact__line">
      <svg viewBox="0 0 12 12" aria-hidden="true"><rect x="1" y="2.5" width="10" height="7" fill="none" stroke="#85acd3" stroke-width="1.2"/><path d="M1 2.5 L6 6.5 L11 2.5" fill="none" stroke="#85acd3" stroke-width="1.2"/></svg>
      <span>info@brellmontrestoration.com</span>
    </div>
    <div class="contact__line contact__web">
      <svg viewBox="0 0 12 12" aria-hidden="true"><circle cx="6" cy="6" r="5" fill="none" stroke="#85acd3" stroke-width="1.1"/><ellipse cx="6" cy="6" rx="2.2" ry="5" fill="none" stroke="#85acd3" stroke-width="1"/><path d="M1 6 H11" stroke="#85acd3" stroke-width="1"/></svg>
      <span>www.<span class="domain">brellmontrestoration</span>.com</span>
    </div>
  </div>
</section>

</body>
</html>
```